New PowerPoint Design Project

A well-known speaker needs a visual presence that compliments his amazing, consistent performance onstage. You'll easily improve this deck, and I'll leave it to you whether you stick with the palette defined by the original BLQEMS icons you'll find in the deck, the mishmosh in the deck as it stands, OR get extra points by going with the corporate color palette so our speaking slides fit with Ronan's brands and his three sub-brands. A look at the Ronan subbrand .png in the attached zip file might give you some ideas.
Updates

Just noting that I'm available to answer questions or supply assets you think you'd need. The big design issue I'm looking for someone to solve is how you'll treat the bright clusters of icons in information graphics of the deck.

Target Market(s)

Corporate Executives and wanabees

Requirements
Must have
• The footer needs to have the Dellwyn Bluepath logo and Twitter and Facebook link and you need to do the first 27 slides. The slides past 27 are there simply if you want to use assets from those slides.
Nice to have
• Use the palette document in the zip rather than palette dictated by the BLQEMS icons in the deck (I do not have source for the icons.).

```html
<!DOCTYPE html>
<html lang="en">
<head>
<meta charset="utf-8">
<title>Our Unique Value Proposition and Point of View</title>
<link href="https://fonts.googleapis.com/css2?family=Graduate&family=Open+Sans:wght@400;600;700&display=swap" rel="stylesheet">
<style>
  :root {
    --page: #ffffff;
    --slide: #f7f9ea;
    --ink: #3a3a3a;
    --grey: #7a7a7a;
    --panel: #58595b;
    --green: #8dc63f;
    --green-dark: #6fa82c;
    --tan: #c89f72;
    --footer: #2e2e2e;
    --footer-box: #3a3a3c;
    --orange: #f0a232;
    --white: #ffffff;
    --badge: #d0d0d0;
    --circle: #e4e4e4;
  }
  * { box-sizing: border-box; margin: 0; padding: 0; }
  html, body { width: 1200px; height: 900px; overflow: hidden; background: var(--page); }
  body { position: relative; font-family: "Open Sans", Arial, sans-serif; }
  .slide { position: absolute; left: 60px; top: 193px; width: 1080px; height: 607px; background: var(--slide); overflow: hidden; }
  .abs { position: absolute; }
  .title { left: 68px; top: 26px; font-family: "Graduate", serif; font-size: 38px; line-height: 46px; color: var(--ink); white-space: nowrap; transform: scaleX(0.77); transform-origin: left center; }
  .title .accent { color: var(--green); }
  .page-badge { left: 1037px; top: 19px; width: 36px; height: 36px; border-radius: 50%; background: var(--badge); color: var(--white); font-weight: 700; font-size: 18px; text-align: center; line-height: 36px; }
  .heading { font-size: 20px; font-weight: 600; color: var(--grey); text-align: center; white-space: nowrap; }
  .subhead { font-size: 11.5px; font-weight: 700; color: var(--green); text-align: center; text-transform: uppercase; width: 246px; }
  .panel { position: absolute; top: 144px; width: 246px; height: 293px; background: var(--panel); border-radius: 10px; overflow: hidden; }
  .panel svg { position: absolute; left: 0; top: 0; }
  .panel-text { position: absolute; left: 0; width: 100%; text-align: center; color: var(--white); }
  .band-label { left: 356px; top: 446px; font-size: 11.5px; font-weight: 700; color: var(--white); }
  .outcome { top: 470px; width: 230px; height: 35px; border-radius: 9px; background: var(--tan); color: var(--white); font-size: 12px; font-weight: 700; text-align: center; line-height: 35px; }
  .footer { left: 0; top: 511px; width: 1080px; height: 89px; background: var(--footer); }
  .footer-strip { left: 0; top: 600px; width: 1080px; height: 7px; background: var(--orange); }
  .follow { left: 2px; top: 516px; width: 325px; height: 80px; background: var(--footer-box); box-shadow: 0 2px 8px rgba(0,0,0,.5); }
  .follow-title { left: 14px; top: 8px; font-size: 13px; font-weight: 700; color: var(--green); }
  .follow-link { left: 18px; font-size: 13px; font-weight: 700; color: var(--white); white-space: nowrap; }
  .follow-link::before { content: ""; display: inline-block; width: 13px; height: 13px; background: var(--grey); margin-right: 8px; vertical-align: -2px; }
  .tagline { left: 360px; top: 551px; font-size: 16.5px; font-weight: 700; color: var(--white); white-space: nowrap; }
  .tagline .muted { color: var(--grey); }
  .brand-box { left: 793px; top: 516px; width: 287px; height: 80px; background: var(--footer-box); box-shadow: 0 2px 8px rgba(0,0,0,.5); }
  .brand-name { left: 20px; top: 22px; font-size: 25px; font-weight: 400; color: var(--white); white-space: nowrap; }
  .brand-name::before { content: ""; display: inline-block; width: 30px; height: 30px; background: var(--white); margin-right: 10px; vertical-align: -6px; }
  svg text { font-family: "Open Sans", Arial, sans-serif; fill: var(--white); }
</style>
</head>
<body>
<main class="slide">
  <h1 class="abs title">OUR UNIQUE VALUE PROPOSITION <span class="accent">AND POINT OF VIEW</span></h1>
  <div class="abs page-badge">18</div>

  <h2 class="abs heading" style="left:20px;top:92px;width:246px;">Change is Hard</h2>
  <h2 class="abs heading" style="left:248px;top:92px;width:510px;">Cultures Don’t Change, People Do</h2>
  <h2 class="abs heading" style="left:780px;top:92px;width:300px;">Non-Traditional Approach</h2>
  <p class="abs subhead" style="left:20px;top:123px;">Highest Return Practices</p>
  <p class="abs subhead" style="left:283px;top:123px;">Open “Porosity”</p>
  <p class="abs subhead" style="left:547px;top:123px;">Role Model Community</p>
  <p class="abs subhead" style="left:812px;top:123px;">Coaching Interventions</p>

  <section class="panel" style="left:20px;">
    <p class="panel-text" style="top:35px;font-size:12px;">Thin slicing behaviors into distinct practices</p>
    <svg width="246" height="293" viewBox="0 0 246 293">
      <rect x="20" y="88" width="78" height="82" fill="var(--green)"/>
      <ellipse cx="20" cy="129" rx="8" ry="41" fill="var(--green)"/>
      <ellipse cx="98" cy="129" rx="8" ry="41" fill="var(--green-dark)"/>
      <text x="28" y="134" font-size="10">BEHAVIORS</text>
      <g fill="var(--green)">
        <rect x="129" y="88" width="8" height="82" rx="4"/>
        <rect x="147" y="88" width="8" height="82" rx="4"/>
        <rect x="165" y="88" width="8" height="82" rx="4"/>
        <rect x="184" y="88" width="8" height="82" rx="4"/>
        <rect x="204" y="88" width="8" height="82" rx="4"/>
      </g>
      <g stroke="var(--white)" stroke-width="1.2" fill="none">
        <path d="M132 178 V208 H216 V178"/>
        <path d="M174 208 V220"/>
      </g>
      <text x="170" y="238" font-size="12" text-anchor="middle">DISTINCT PRACTICES</text>
    </svg>
  </section>

  <section class="panel" style="left:283px;">
    <p class="panel-text" style="top:16px;font-size:12px;line-height:15px;">Create openness to changing and adopting<br>new behaviors &amp; practices</p>
    <svg width="246" height="293" viewBox="0 0 246 293">
      <g fill="var(--green)">
        <rect x="35" y="71" width="4" height="157"/>
        <path d="M27 76 L37 64 L47 76 Z"/>
        <rect x="35" y="224" width="191" height="4"/>
        <path d="M222 216 L235 226 L222 236 Z"/>
        <rect x="42" y="186" width="35" height="34"/>
        <rect x="79" y="168" width="34" height="52"/>
        <rect x="115" y="149" width="36" height="71"/>
        <rect x="153" y="132" width="35" height="88"/>
        <rect x="190" y="115" width="35" height="105"/>
      </g>
      <g font-size="5">
        <text x="59" y="183" text-anchor="middle">consequences</text>
        <text x="96" y="165" text-anchor="middle">logic</text>
        <text x="133" y="146" text-anchor="middle">ease</text>
        <text x="170" y="129" text-anchor="middle">passion</text>
        <text x="207" y="112" text-anchor="middle">belonging</text>
      </g>
      <g font-size="7">
        <text transform="translate(23 122) rotate(-90)">EMOTIONAL</text>
        <text transform="translate(23 230) rotate(-90)">INTELLECTUAL</text>
        <text x="33" y="243">EXTERNAL</text>
        <text x="221" y="243" text-anchor="end">INTERNAL</text>
      </g>
    </svg>
  </section>

  <section class="panel" style="left:547px;">
    <p class="panel-text" style="top:9px;font-size:15.5px;line-height:20px;">Engage early role models as<br>an early organizing movement</p>
    <svg width="246" height="293" viewBox="0 0 246 293">
      <circle cx="123" cy="175" r="85" fill="var(--circle)"/>
      <rect x="98" y="150" width="50" height="52" rx="6" fill="#9cc4e4" role="img" aria-label="Small group of role model figures with a leader raised above"/>
    </svg>
  </section>

  <section class="panel" style="left:812px;">
    <p class="panel-text" style="top:9px;font-size:9.5px;line-height:12px;">Use coaching, not training and communications<br>as the key change lever</p>
    <svg width="246" height="293" viewBox="0 0 246 293">
      <g fill="var(--green)">
        <path d="M6 49 H160 L172 61 L160 73 H6 L14 61 Z"/>
        <path d="M6 82 H160 L172 94 L160 106 H6 L14 94 Z"/>
        <path d="M6 115 H160 L172 127 L160 139 H6 L14 127 Z"/>
        <path d="M6 151 H160 L172 163 L160 175 H6 L14 163 Z"/>
        <path d="M6 182 H160 L172 194 L160 206 H6 L14 194 Z"/>
        <path d="M6 216 H160 L172 228 L160 240 H6 L14 228 Z"/>
        <path d="M6 248 H160 L172 260 L160 272 H6 L14 260 Z"/>
        <path d="M181 58 L193 46 L205 58 V276 L193 264 L181 276 Z"/>
        <path d="M214 58 L226 46 L238 58 V276 L226 264 L214 276 Z"/>
      </g>
      <g font-size="12" text-anchor="middle">
        <text x="88" y="66">VIRTUAL</text>
        <text x="88" y="99">PEER COMMUNITY</text>
        <text x="88" y="132">SELF-DIRECTED</text>
        <text x="88" y="168">CUSTOMER</text>
        <text x="88" y="199">MANAGERIAL</text>
        <text x="88" y="233">EXPERT</text>
        <text x="88" y="265">TECHNOLOGY ENABLED</text>
        <text transform="translate(197 170) rotate(-90)">PRACTICES</text>
        <text transform="translate(230 170) rotate(-90)">CELEBRATION</text>
      </g>
    </svg>
  </section>

  <svg class="abs" style="left:0;top:442px;" width="1080" height="24" viewBox="0 0 1080 24">
    <path d="M0 0 H1052 L1066 12 L1052 24 H0 L10 12 Z" fill="var(--ink)"/>
    <path d="M0 0 H126 V24 H0 L10 12 Z" fill="var(--green)"/>
  </svg>
  <p class="abs band-label">BEHAVIOR CHANGE IN SERVICE OF BUSINESS OUTCOMES</p>

  <div class="abs outcome" style="left:28px;">Customer Experience</div>
  <div class="abs outcome" style="left:291px;">Strategic Account Management</div>
  <div class="abs outcome" style="left:554px;">High Impact Teams</div>
  <div class="abs outcome" style="left:822px;">Self Directed Learning</div>

  <footer>
    <div class="abs footer"></div>
    <div class="abs footer-strip"></div>
    <div class="abs follow">
      <p class="abs follow-title">FOLLOW ME ON :</p>
      <p class="abs follow-link" style="top:32px;">https://www.friendwall.com/ronandellwyn</p>
      <p class="abs follow-link" style="top:54px;">https://www.chirpline.com/dellwyn</p>
    </div>
    <p class="abs tagline">Business is Human | <span class="muted">Relationships Power Growth.</span></p>
    <div class="abs brand-box">
      <p class="abs brand-name">dellwynbluepath</p>
    </div>
  </footer>
</main>
</body>
</html>
```